Recruitment website for new startup company - Tal Brisk Recruitment

Hi , I need to design a web page for my new recruitment company with the ability to link to social media accounts. The ability to add and remove job posts along with a blog page which I can update. More importantly I need the website to have the functionality of applicants being able to upload their cv and somewhere for me to store it. I will need assistance/recommendation for email address with company name, hosting and security. An about us page. The website will also need a search function for applicants to narrow down the search. Again I will need to be able to update this myself as the company grows. I have my logo ready domain address ready and would like the web site done ASAP. Thank you for your help.
Updates

Project Deadline Extended
Reason: Want to get a few more ideas and variations to designs done. But using logo as inspiration Thanks

Target Market(s)

Financial and property industry so professionals. New starters to senior management age range 25-60

Industry/Entity Type

Financial

Coding

Coded - Design and coding required

Number of Pages Required

4 page

Colors

Designer to choose colors to be used in the design.

Requirements
Must have
• Ability for me to add amend and remove job posts, ability for applicants to upload cv and for me to store and access it. Link to social media accounts
Should not have
• Needs to be clean approachable so not to childish but must come across as approachable and trustworthy.
• No yellow please my logo has a gold V not yellow. If it looks yellow use a different colour please. Thanks

```html
<!DOCTYPE html>
<html lang="en">
<head>
<meta charset="utf-8">
<title>Tal Brisk Recruitment</title>
<link href="https://fonts.googleapis.com/css2?family=Mulish:wght@400;600;700;800&family=Open+Sans:wght@400;600&display=swap" rel="stylesheet">
<style>
:root{
  --navy:#1d2f55;
  --navy-dark:#16264a;
  --gold:#9a7a45;
  --gold-deep:#86693a;
  --gold-soft:#efe3cc;
  --grey-band:#efefef;
  --grey-card:#f0f0f0;
  --line:#dcdcdc;
  --text:#3b3b3b;
  --muted:#6c6c6c;
  --white:#ffffff;
  --news:#353535;
  --foot:#2b2b2b;
}
*{box-sizing:border-box;margin:0;padding:0}
html,body{width:1200px;height:3010px;overflow:hidden}
body{position:relative;background:var(--white);font-family:"Open Sans",Arial,sans-serif;color:var(--text)}
h1,h2,h3,h4{font-family:"Mulish",Arial,sans-serif}

/* header */
.site-header{position:absolute;left:0;top:0;width:1200px;height:138px}
.brand{position:absolute;left:132px;top:40px;font-family:"Mulish",Arial,sans-serif;font-weight:700;color:var(--navy);text-align:center;line-height:1}
.brand .brand-name{font-size:34px;letter-spacing:1px}
.brand .brand-sub{font-size:15px;letter-spacing:4.6px;margin-top:8px}
.account{position:absolute;top:26px;height:36px;border:1px solid #d5d5d5;font-size:11px;color:#8a8a8a;display:flex;align-items:center;justify-content:center;gap:6px}
.account.login{left:898px;width:70px}
.account.register{left:976px;width:88px}
.main-nav{position:absolute;top:88px;right:136px;display:flex;font-size:14px;font-family:"Mulish",Arial,sans-serif}
.main-nav a{color:#555;text-decoration:none;margin-left:42px}
.main-nav a.active{color:var(--gold)}

/* hero */
.hero{position:absolute;top:138px;left:0;width:1200px;height:474px}
.hero-photo{position:absolute;left:0;top:0;width:750px;height:474px;background:linear-gradient(100deg,#c9ccd0 0%,#8c8f95 35%,#3c3f46 55%,#d5d4d2 80%,#b9b5b2 100%)}
.slide-arrow{position:absolute;top:222px;width:24px;height:32px;background:rgba(40,40,40,.55);display:flex;align-items:center;justify-content:center}
.hero-panel{position:absolute;left:750px;top:0;width:450px;height:474px;background:var(--gold)}
.hero-panel h1{position:absolute;left:30px;top:66px;font-size:24px;line-height:30px;font-weight:800;color:var(--white);text-transform:uppercase}
.hero-panel .lead{position:absolute;left:32px;top:130px;width:290px;font-size:13px;line-height:19px;color:var(--gold-soft)}
.field{position:absolute;left:32px;width:270px;height:40px;background:var(--white);font-size:11px;color:#777;padding:0 12px;display:flex;align-items:center;justify-content:space-between}
.btn-search{position:absolute;left:32px;top:360px;width:90px;height:42px;background:var(--navy);color:var(--white);font-family:"Mulish",Arial,sans-serif;font-weight:800;font-size:14px;display:flex;align-items:center;justify-content:center}

/* steps */
.steps{position:absolute;top:612px;left:0;width:1200px;height:304px;background:var(--grey-band);text-align:center}
.section-title{font-family:"Mulish",Arial,sans-serif;font-weight:700;font-size:24px;color:var(--navy-dark)}
.steps .section-title{position:absolute;top:54px;left:0;width:1200px}
.steps .sub{position:absolute;top:92px;left:0;width:1200px;font-size:14px;color:#555}
.steps .track{position:absolute;left:406px;top:173px;width:386px;height:4px;background:var(--line)}
.step{position:absolute;top:136px;width:120px;text-align:center}
.step .circle{width:80px;height:80px;margin:0 auto;border-radius:50%;background:var(--white);box-shadow:0 2px 6px rgba(0,0,0,.08);display:flex;align-items:center;justify-content:center}
.step .label{margin-top:18px;font-family:"Mulish",Arial,sans-serif;font-size:18px;font-weight:600;color:var(--navy)}

/* featured */
.featured-title{position:absolute;top:990px;left:0;width:1200px;text-align:center}
.featured-card{position:absolute;top:1042px;left:132px;width:932px;height:278px}
.featured-photo{position:absolute;left:0;top:0;width:466px;height:278px;background:linear-gradient(120deg,#6f4a34 0%,#b7906f 40%,#e6ddd6 60%,#7a6a5e 100%)}
.featured-body{position:absolute;left:466px;top:0;width:466px;height:278px;background:var(--grey-card);padding:38px 24px 0 36px}
.featured-body h3{font-size:20px;font-weight:600;color:var(--navy-dark)}
.meta{font-size:12px;color:#666}
.featured-body .salary{margin-top:18px;font-size:13px;color:#222}
.featured-body .desc{margin-top:16px;font-size:10.5px;line-height:17px;color:#555}
.featured-body .desc b{color:#222}

/* recent jobs */
.recent-title{position:absolute;top:1394px;left:0;width:1200px;text-align:center}
.job-card{position:absolute;top:1446px;width:220px;height:234px;background:var(--white);box-shadow:0 1px 5px rgba(0,0,0,.14);padding:24px 20px}
.job-card h4{font-size:15px;line-height:19px;font-weight:700;color:var(--navy-dark)}
.job-card .meta{margin-top:4px;font-size:11px}
.job-card .time{margin-top:16px;font-size:11px;color:#666}
.job-card .salary{margin-top:16px;font-size:13px;color:#222}
.job-card .type{margin-top:6px;font-size:12px;color:#666}
.job-card .more{position:absolute;left:20px;bottom:24px;width:80px;height:34px;border:1px solid #cfcfcf;font-size:10px;color:#666;display:flex;align-items:center;justify-content:center}
.view-all{position:absolute;top:1706px;left:546px;width:106px;height:38px;background:#e7e7e7;font-size:11px;color:#888;display:flex;align-items:center;justify-content:center;font-family:"Mulish",Arial,sans-serif}

/* upload */
.upload{position:absolute;top:1824px;left:0;width:1200px;height:376px;background:linear-gradient(90deg,#3f5260 0%,#566b78 55%,#6c808c 100%)}
.upload-photo{position:absolute;left:680px;top:0;width:520px;height:376px;background:linear-gradient(90deg,rgba(108,128,140,0) 0%,#8b8682 40%,#6b5a4f 70%,#7a8c96 100%)}
.upload h2{position:absolute;left:132px;top:96px;font-size:24px;font-weight:700;color:var(--white)}
.upload p{position:absolute;left:132px;top:134px;width:420px;font-size:11.5px;line-height:17px;color:#c9d0d6}
.upload .file{position:absolute;left:132px;top:182px;width:272px;height:40px;background:var(--white);font-size:11px;color:#555;display:flex;align-items:center;justify-content:space-between;padding:0 14px 0 18px}
.btn-upload{position:absolute;left:132px;top:238px;width:96px;height:38px;background:var(--gold);color:var(--white);font-family:"Mulish",Arial,sans-serif;font-weight:800;font-size:14px;display:flex;align-items:center;justify-content:center}

/* blog */
.blog-title{position:absolute;top:2272px;left:0;width:1200px;text-align:center}
.post{position:absolute;top:2322px;width:296px;height:384px;background:var(--grey-card)}
.post .thumb{width:296px;height:198px}
.post .post-body{padding:22px 22px}
.post h4{font-size:16px;line-height:21px;font-weight:600;color:#333}
.post p{margin-top:8px;font-size:11px;line-height:16px;color:#777}
.post .read{display:inline-block;margin-top:20px;font-size:10px;font-weight:600;color:#333;text-decoration:underline}
.blog-arrow{position:absolute;top:2500px}

/* newsletter */
.newsletter{position:absolute;top:2784px;left:0;width:1200px;height:96px;background:var(--news)}
.newsletter .label{position:absolute;left:246px;top:30px;display:flex;align-items:center;gap:10px;font-family:"Mulish",Arial,sans-serif;font-weight:700;font-size:24px;color:var(--white)}
.newsletter .email{position:absolute;left:598px;top:28px;width:238px;height:40px;background:var(--white);font-size:11px;color:#444;padding-left:18px;display:flex;align-items:center}
.newsletter .subscribe{position:absolute;left:836px;top:28px;width:112px;height:40px;background:var(--gold);font-family:"Mulish",Arial,sans-serif;font-weight:800;font-size:14px;color:var(--white);display:flex;align-items:center;justify-content:center}

/* footer */
.site-footer{position:absolute;top:2880px;left:0;width:1200px;height:130px;background:var(--foot)}
.foot-links{position:absolute;left:132px;top:36px;font-size:12px;color:#bbb}
.foot-links span{margin:0 8px;color:#888}
.copyright{position:absolute;left:132px;top:66px;font-size:12px;color:#999}
.social{position:absolute;left:942px;top:34px;display:flex;gap:9px}
.social i{display:block;width:24px;height:24px;border-radius:50%;background:#5d6a78}
</style>
</head>
<body>

<header class="site-header">
  <div class="brand"><div class="brand-name">TAL BRISK</div><div class="brand-sub">RECRUITMENT</div></div>
  <div class="account login">
    <svg width="10" height="10" viewBox="0 0 10 10"><path d="M1 5h5M4 2.5L6.5 5 4 7.5M7 1h2v8H7" fill="none" stroke="#888" stroke-width="1.2"/></svg>Login
  </div>
  <div class="account register">
    <svg width="10" height="10" viewBox="0 0 10 10"><path d="M1.5 8.5l1-3 5-5 2 2-5 5z" fill="#888"/></svg>Register
  </div>
  <nav class="main-nav"><a class="active" href="#">HOME</a><a href="#">ABOUT</a><a href="#">RECRUITMENT</a><a href="#">NEWS</a><a href="#">CONTACT</a></nav>
</header>

<section class="hero">
  <div class="hero-photo" role="img" aria-label="Photo of a smiling businessman in a suit shaking hands across a desk"></div>
  <div class="slide-arrow" style="left:0"><svg width="8" height="12" viewBox="0 0 8 12"><path d="M6 1L1 6l5 5" fill="none" stroke="#fff" stroke-width="1.5"/></svg></div>
  <div class="slide-arrow" style="left:726px"><svg width="8" height="12" viewBox="0 0 8 12"><path d="M2 1l5 5-5 5" fill="none" stroke="#fff" stroke-width="1.5"/></svg></div>
  <div class="hero-panel">
    <h1>Multi-Industry<br>Recruitment Agency</h1>
    <p class="lead">Duis ornare erat eget magna dapibus, in accumsan quam pharetra</p>
    <div class="field" style="top:192px">Job Keywords</div>
    <div class="field" style="top:248px">Locations</div>
    <div class="field" style="top:304px">Sector<svg width="9" height="6" viewBox="0 0 9 6"><path d="M1 1l3.5 3.5L8 1" fill="none" stroke="#555" stroke-width="1.2"/></svg></div>
    <div class="btn-search">SEARCH</div>
  </div>
</section>

<section class="steps">
  <h2 class="section-title">All the jobs you want in one simple place</h2>
  <p class="sub">Vestibulum condimentum, risus ut posuere cursus</p>
  <div class="track"></div>
  <div class="step" style="left:346px">
    <div class="circle"><svg width="22" height="22" viewBox="0 0 22 22"><circle cx="9" cy="9" r="6.5" fill="none" stroke="#1d2f55" stroke-width="2.6"/><path d="M14 14l6 6" stroke="#1d2f55" stroke-width="3" stroke-linecap="round"/></svg></div>
    <div class="label">SEARCH</div>
  </div>
  <div class="step" style="left:540px">
    <div class="circle"><svg width="24" height="22" viewBox="0 0 24 22"><path d="M15 4H3v15h15v-7" fill="none" stroke="#1d2f55" stroke-width="2"/><path d="M9 14l1-4 9-9 3 3-9 9z" fill="none" stroke="#1d2f55" stroke-width="2"/></svg></div>
    <div class="label">APPLY</div>
  </div>
  <div class="step" style="left:734px">
    <div class="circle"><svg width="24" height="22" viewBox="0 0 24 22"><rect x="8" y="2" width="8" height="5" fill="none" stroke="#1d2f55" stroke-width="2"/><rect x="1" y="6" width="22" height="14" rx="2" fill="#1d2f55"/><rect x="10" y="11" width="4" height="3" fill="#fff"/></svg></div>
    <div class="label">HIRED</div>
  </div>
</section>

<h2 class="section-title featured-title">Featured Job</h2>
<article class="featured-card">
  <div class="featured-photo" role="img" aria-label="Photo of a smiling restaurant manager with diners behind her"></div>
  <div class="featured-body">
    <h3>Steak House Manager</h3>
    <div class="meta">Neatherlands, Rotterdam</div>
    <div class="salary">£ 27500 - £ 30000</div>
    <div class="meta" style="margin-top:4px">Full Time</div>
    <p class="desc">Fusce sollicitudin lorem et luctus volutpat. Proin placerat dapibus gravida. In tristique tristique nulla eget hendrerit. Maecenas vel tortor accumsan quam varius imperdiet vel eget elit. Aenean facilisis tincidunt lectus, id dictum nisi luctus eget. Vivamus efficitur ex condimentum, malesuada eros eget, feugiat nibh. Sed tellus ex, imperdiet eget gravida sit amet, volutpat eget turpis. <b>More</b></p>
  </div>
</article>

<h2 class="section-title recent-title">Recent Jobs</h2>
<article class="job-card" style="left:132px">
  <h4>Sales &amp; Marketing Coordinator</h4>
  <div class="meta">Germany, Hanover</div>
  <div class="time" style="margin-top:6px">65 Days 21:66:59</div>
  <div class="salary">£ 27500</div>
  <div class="type">Full Time</div>
  <div class="more">View More</div>
</article>
<article class="job-card" style="left:372px">
  <h4>Engineering Technician</h4>
  <div class="meta" style="margin-top:23px">Neatherlands, Rotterdam</div>
  <div class="time" style="margin-top:6px">65 Days 21:66:59</div>
  <div class="salary">£ 27500</div>
  <div class="type">Full Time</div>
  <div class="more">View More</div>
</article>
<article class="job-card" style="left:610px">
  <h4>Science Teacher</h4>
  <div class="meta" style="margin-top:23px">England, London</div>
  <div class="time" style="margin-top:6px">65 Days 21:66:59</div>
  <div class="salary">£ 27500</div>
  <div class="type">Full Time</div>
  <div class="more">View More</div>
</article>
<article class="job-card" style="left:848px">
  <h4>Accounts Assistant</h4>
  <div class="meta" style="margin-top:23px">England, Hampsire</div>
  <div class="time" style="margin-top:6px">65 Days 21:66:59</div>
  <div class="salary">£ 27500</div>
  <div class="type">Full Time</div>
  <div class="more">View More</div>
</article>
<div class="view-all">VIEW ALL</div>

<section class="upload">
  <div class="upload-photo" role="img" aria-label="Photo of a smiling woman in glasses holding up a printed resume"></div>
  <h2>Upload Your Resume</h2>
  <p>Aliquam erat volutpat. Quisque aliquet ex nec est vestibulum pulvinar. Pellentesque convallis molestie enim sit amet efficitur.</p>
  <div class="file">Select File<svg width="14" height="11" viewBox="0 0 14 11"><path d="M0 1h5l1 1.5h6V4H3L0 10z" fill="#444"/><path d="M3 5h11l-3 6H0z" fill="#444"/></svg></div>
  <div class="btn-upload">UPLOAD</div>
</section>

<h2 class="section-title blog-title">Blog</h2>
<svg class="blog-arrow" style="left:38px" width="14" height="28" viewBox="0 0 14 28"><path d="M12 2L2 14l10 12" fill="none" stroke="#bbb" stroke-width="2.5"/></svg>
<svg class="blog-arrow" style="left:1140px" width="14" height="28" viewBox="0 0 14 28"><path d="M2 2l10 12L2 26" fill="none" stroke="#bbb" stroke-width="2.5"/></svg>
<article class="post" style="left:132px">
  <div class="thumb" role="img" aria-label="Photo of hands writing in a notebook on a wooden desk" style="background:linear-gradient(135deg,#3a2a1e 0%,#7a5a3e 50%,#c9b29a 100%)"></div>
  <div class="post-body">
    <h4>Maecenas vel tortor accumsan quam varius imperdiet</h4>
    <p>Aliquam consectetur orci molestie dictum moles-tie. Proin eget congue nulla, vel tempor diam risus ut posuere cursus, velit.</p>
    <span class="read">READ MORE</span>
  </div>
</article>
<article class="post" style="left:450px">
  <div class="thumb" role="img" aria-label="Photo of two colleagues talking at a desk with a laptop" style="background:linear-gradient(135deg,#eceae6 0%,#c8c3bd 45%,#5a5e6a 100%)"></div>
  <div class="post-body">
    <h4>Aenean facilisis tincidunt lectus, id dictum nisi</h4>
    <p>Aliquam consectetur orci molestie dictum moles-tie. Proin eget congue nulla, vel tempor diam risus ut posuere cursus, velit.</p>
    <span class="read">READ MORE</span>
  </div>
</article>
<article class="post" style="left:768px">
  <div class="thumb" role="img" aria-label="Photo of a man in glasses working on a laptop on a sofa" style="background:linear-gradient(135deg,#b08a66 0%,#6b6e74 50%,#3d3a38 100%)"></div>
  <div class="post-body">
    <h4>Etiam mattis augue vehicula odio posuere, sit amet</h4>
    <p>Aliquam consectetur orci molestie dictum moles-tie. Proin eget congue nulla, vel tempor diam risus ut posuere cursus, velit.</p>
    <span class="read">READ MORE</span>
  </div>
</article>

<section class="newsletter">
  <div class="label"><svg width="22" height="16" viewBox="0 0 22 16"><rect x="1" y="1" width="20" height="14" rx="2" fill="none" stroke="#fff" stroke-width="2"/><path d="M1.5 2l9.5 7 9.5-7" fill="none" stroke="#fff" stroke-width="2"/></svg>NEWSLETTER SUBSCRIBE</div>
  <div class="email">Email Address</div>
  <div class="subscribe">SUBSCRIBE</div>
</section>

<footer class="site-footer">
  <div class="foot-links">Home<span>|</span>About<span>|</span>Recruitment<span>|</span>News<span>|</span>Contact</div>
  <div class="copyright">Copyright © 2017 Tal Brisk Recruitment. &nbsp;All rights reserved.</div>
  <div class="social" aria-label="Social media links"><i></i><i></i><i></i><i></i></div>
</footer>

</body>
</html>
```